Workvine banner ad for roofing company

We need an ad created for a Workvine banner advertising campaign for a UK based roofing company.

The design should have a large photograph on the background (see attached).
The design should have our Ratewell rating (5 stars).
There should be a large text header at the top which reads "Your local roofing experts"

The following services should be listed:
- New roofs
- General roof repairs
- Drone surveys
- Single ply roofing
- Steel cladding
- Asbestos removal

The company logo needs to be visible (attached). Also the company telephone number 020 7946 0321 and website www.brantleyroofing.com

The advert needs to be horizontal/landscape design. For full spec, please see here: https://business.workvine-example.com/marketing-solutions/success/ads-guide/single-image-ads

Size required: 1.91:1 - 1200 x 628 pixels

```html
<!DOCTYPE html>
<html lang="en">
<head>
<meta charset="utf-8">
<title>Brantley Roofing – Your Local Roofing Experts</title>
<link rel="stylesheet" href="https://fonts.googleapis.com/css2?family=Poppins:wght@300;400;500;600&display=swap">
<style>
  :root {
    --brand-blue: #1d5690;
    --brand-blue-deep: #164a7e;
    --accent-cyan: #27a9e1;
    --white: #ffffff;
    --photo-grey: #9aa3a6;
    --photo-green: #6f8a55;
    --photo-brick: #b88a63;
  }
  * { margin: 0; padding: 0; box-sizing: border-box; }
  html, body { width: 1200px; height: 628px; overflow: hidden; background: var(--white); }
  body { font-family: "Poppins", Arial, sans-serif; color: var(--white); }

  .banner { position: relative; width: 1200px; height: 628px; overflow: hidden; }

  .aerial-photo {
    position: absolute; inset: 0;
    background:
      radial-gradient(ellipse at 75% 40%, var(--photo-brick) 0%, transparent 35%),
      radial-gradient(ellipse at 60% 70%, var(--photo-green) 0%, transparent 45%),
      linear-gradient(135deg, var(--photo-grey) 0%, #b7bdbd 45%, #8a9a80 100%);
  }

  .panel-shape { position: absolute; inset: 0; }

  .headline { position: absolute; left: 57px; top: 36px; font-size: 62px; line-height: 1.18; letter-spacing: -0.5px; }
  .headline .light { display: block; font-weight: 300; }
  .headline .bold { display: block; font-weight: 600; }

  .services { position: absolute; left: 57px; top: 232px; list-style: none; }
  .services li { display: flex; align-items: center; height: 40px; font-size: 22px; font-weight: 400; }
  .services svg { width: 18px; height: 18px; margin-right: 14px; }

  .rating { position: absolute; left: 57px; top: 538px; display: flex; align-items: center; gap: 14px; }
  .rating-text { font-size: 13px; line-height: 1.4; }
  .rating-badge { display: flex; flex-direction: column; gap: 4px; }
  .rating-name { font-size: 16px; font-weight: 500; }
  .rating-boxes { display: flex; gap: 2px; }
  .rating-boxes span { width: 19px; height: 19px; background: var(--white); }

  .call { position: absolute; left: 311px; top: 536px; display: flex; align-items: center; gap: 14px; }
  .call-icon { width: 44px; height: 44px; }
  .call-label { font-size: 15px; line-height: 1.2; }
  .call-number { font-size: 22px; font-weight: 600; line-height: 1.3; }

  .brand-badge {
    position: absolute; left: 437px; top: 232px; width: 206px; height: 206px;
    border-radius: 50%; background: var(--white);
    display: flex; flex-direction: column; align-items: center; justify-content: center;
  }
  .brand-mark { width: 34px; height: 34px; border-radius: 50%; background: var(--accent-cyan); margin-bottom: 8px; }
  .brand-name { font-size: 22px; font-weight: 600; color: var(--brand-blue); line-height: 1.1; text-align: center; }
  .brand-site { font-size: 15px; color: var(--brand-blue-deep); margin-top: 14px; }
</style>
</head>
<body>
<div class="banner">
  <div class="aerial-photo" role="img" aria-label="Aerial drone photo of flat-roofed brick residential blocks with lawns and paths"></div>

  <svg class="panel-shape" viewBox="0 0 1200 628" aria-hidden="true">
    <path d="M0 0 H610 Q468 314 610 628 H0 Z" fill="var(--brand-blue)" fill-opacity="0.93"/>
    <path d="M622 0 Q480 314 622 628" fill="none" stroke="var(--accent-cyan)" stroke-width="7"/>
  </svg>

  <h1 class="headline">
    <span class="light">Your Local</span>
    <span class="bold">Roofing Experts</span>
  </h1>

  <ul class="services">
    <li><svg viewBox="0 0 18 18"><path d="M2 9.5 L7 14 L16 3" fill="none" stroke="#fff" stroke-width="2.4" stroke-linecap="round" stroke-linejoin="round"/></svg>New roofs</li>
    <li><svg viewBox="0 0 18 18"><path d="M2 9.5 L7 14 L16 3" fill="none" stroke="#fff" stroke-width="2.4" stroke-linecap="round" stroke-linejoin="round"/></svg>General roof repairs</li>
    <li><svg viewBox="0 0 18 18"><path d="M2 9.5 L7 14 L16 3" fill="none" stroke="#fff" stroke-width="2.4" stroke-linecap="round" stroke-linejoin="round"/></svg>Drone surveys</li>
    <li><svg viewBox="0 0 18 18"><path d="M2 9.5 L7 14 L16 3" fill="none" stroke="#fff" stroke-width="2.4" stroke-linecap="round" stroke-linejoin="round"/></svg>Single ply roofing</li>
    <li><svg viewBox="0 0 18 18"><path d="M2 9.5 L7 14 L16 3" fill="none" stroke="#fff" stroke-width="2.4" stroke-linecap="round" stroke-linejoin="round"/></svg>Steel cladding</li>
    <li><svg viewBox="0 0 18 18"><path d="M2 9.5 L7 14 L16 3" fill="none" stroke="#fff" stroke-width="2.4" stroke-linecap="round" stroke-linejoin="round"/></svg>Asbestos removal</li>
  </ul>

  <div class="rating">
    <p class="rating-text">39/5 Star<br>Reviews On</p>
    <div class="rating-badge">
      <span class="rating-name">Ratewell</span>
      <div class="rating-boxes" aria-label="5 out of 5"><span></span><span></span><span></span><span></span><span></span></div>
    </div>
  </div>

  <div class="call">
    <svg class="call-icon" viewBox="0 0 44 44" aria-hidden="true">
      <circle cx="22" cy="22" r="22" fill="#fff"/>
      <path d="M13 19 Q22 13 31 19 L29 22 L26 21 L25.5 18.5 Q22 17.5 18.5 18.5 L18 21 L15 22 Z" fill="var(--brand-blue)"/>
      <rect x="15" y="23" width="14" height="9" rx="2" fill="var(--brand-blue)"/>
      <circle cx="22" cy="27.5" r="2.6" fill="#fff"/>
    </svg>
    <div>
      <p class="call-label">Call us on</p>
      <p class="call-number">020 7946 0321</p>
    </div>
  </div>

  <div class="brand-badge">
    <span class="brand-mark" aria-hidden="true"></span>
    <span class="brand-name">brantley roofing</span>
    <span class="brand-site">brantleyroofing.com</span>
  </div>
</div>
</body>
</html>
```